Create for us a Shop-Stopper Business Card

We need a standout, first class business card to go along with our new brand strategy. Sleek, Contemporary and fresh.

Colors and theme must sync with our websitewww.pelvorpower.co.uk

We want a business card that has a global brand appeal. TKR Energy is a small UK renewable company that specialises in energy projects in Africa. We want a business card that has the following characteristics: Very short, precise, global, stand out, NOT TOO LOUD but contemporary. The company's colour themes are White, Grey with a hint of green.

Target Market(s)

Business exec, high net worth individuals, investors, commercial leaders, suppliers, government officials

Industry/Entity Type

Solar Energy

Contact Information for Business Card

Logo, Name, Title, Address, web address, email,

Requirements
Must have
• Logo must be sharp
Nice to have
• Adapt fonts from the logo. The large circular side of the logo at the back in a very refreshing way
Should not have
• No solar panel shapes or image.Very little black. If possible avoid black. Its not coming out nice. I think !!!

```html
<!DOCTYPE html>
<html lang="en">
<head>
<meta charset="utf-8">
<title>TKR Energy Business Card</title>
<link href="https://fonts.googleapis.com/css2?family=Jost:wght@300;400&family=Open+Sans:wght@400;600&display=swap" rel="stylesheet">
<style>
  :root {
    --page-bg: #eceae6;
    --brand-green: #4b8653;
    --avatar-fill: #3f7a6c;
    --avatar-ring: #d8dcd9;
    --strip-grey: #e1e3e2;
    --card-white: #fbfbfa;
    --text-green: #2f6c40;
    --icon-grey: #4c5c58;
    --light-text: #f1f4f1;
  }
  * { box-sizing: border-box; margin: 0; padding: 0; }
  html, body { width: 1200px; height: 981px; overflow: hidden; }
  body { background: var(--page-bg); position: relative; font-family: "Open Sans", sans-serif; }

  .card {
    position: absolute; left: 190px; width: 820px; height: 410px;
    box-shadow: 0 8px 24px rgba(60,50,40,.18); overflow: hidden;
  }
  .card--front { top: 60px; background: var(--card-white); display: flex; }
  .card--back { top: 511px; background: var(--brand-green); display: flex; align-items: center; justify-content: center; }

  .identity-panel {
    width: 335px; background: var(--brand-green);
    display: flex; flex-direction: column; align-items: center; padding-top: 62px;
  }
  .portrait {
    width: 190px; height: 190px; border-radius: 50%;
    background: radial-gradient(circle at 50% 45%, var(--avatar-fill) 0 48%, var(--avatar-ring) 49%);
    border: 10px solid rgba(255,255,255,.08);
  }
  .person-name {
    margin-top: 30px; font-family: "Jost", sans-serif; font-weight: 300;
    font-size: 38px; letter-spacing: 2px; color: var(--light-text); text-transform: uppercase;
  }
  .person-title {
    margin-top: 2px; font-family: "Jost", sans-serif; font-weight: 300;
    font-size: 19px; letter-spacing: 2px; color: var(--light-text); font-variant: small-caps;
  }

  .icon-strip {
    width: 95px; background: var(--strip-grey);
    display: flex; flex-direction: column; align-items: center; justify-content: center; gap: 58px;
  }
  .icon { width: 26px; height: 26px; fill: var(--icon-grey); }

  .contact-details {
    flex: 1; padding: 120px 0 0 58px; color: var(--text-green);
    font-size: 15px; line-height: 1.4; letter-spacing: .5px;
  }
  .contact-group { margin-bottom: 46px; }
  .contact-group--web { font-weight: 600; font-size: 14px; }
  .address { text-transform: uppercase; }

  .brand-lockup { display: flex; align-items: center; gap: 18px; color: var(--light-text); }
  .brand-mark { width: 68px; height: 68px; border: 5px solid var(--light-text); border-radius: 50%; }
  .brand-name { font-family: "Jost", sans-serif; font-weight: 400; font-size: 62px; letter-spacing: 3px; }
</style>
</head>
<body>
  <section class="card card--front">
    <div class="identity-panel">
      <div class="portrait" role="img" aria-label="Portrait photo of the card holder"></div>
      <h1 class="person-name">John Halden</h1>
      <p class="person-title">Managing Director</p>
    </div>
    <div class="icon-strip">
      <svg class="icon" viewBox="0 0 24 24" aria-label="Phone"><path d="M6.6 10.8a15 15 0 0 0 6.6 6.6l2.2-2.2a1 1 0 0 1 1-.25 11.4 11.4 0 0 0 3.6.57 1 1 0 0 1 1 1V20a1 1 0 0 1-1 1A17 17 0 0 1 3 4a1 1 0 0 1 1-1h3.5a1 1 0 0 1 1 1c0 1.25.2 2.45.57 3.57a1 1 0 0 1-.25 1z"/></svg>
      <svg class="icon" viewBox="0 0 24 24" aria-label="Address"><path d="M12 3 2 12h3v8h5v-5h4v5h5v-8h3z"/></svg>
      <svg class="icon" viewBox="0 0 24 24" aria-label="Website"><circle cx="12" cy="12" r="10"/><path d="M8 6c2 1 3 3 1 5s-3 3-1 6M15 5c-1 2 1 3 3 3M14 14c2 0 3 2 2 4" stroke="#e1e3e2" stroke-width="1.6" fill="none"/></svg>
    </div>
    <div class="contact-details">
      <div class="contact-group">
        <p>+18 2400 5100 6200</p>
        <p>+18 2400 5100 6300</p>
      </div>
      <div class="contact-group address">
        <p>Your City Address</p>
        <p>Street Location, NY City, USA</p>
      </div>
      <div class="contact-group contact-group--web">
        <p>WWW.TKRENERGY.COM</p>
      </div>
    </div>
  </section>

  <section class="card card--back">
    <div class="brand-lockup">
      <span class="brand-mark"></span>
      <span class="brand-name">TKR ENERGY</span>
    </div>
  </section>
</body>
</html>
```